Business Card Design

Hello,
I try and keep my business card fresh and current. So about every year i get a new one. This year I'd like something with a white background and black lettering.
Before you start - I do not want my phone number or any other description on the card other than my url and my email.

I'd like a double sided business card with
TedMarlow.com on one side

and

Ted@TedMarlow.com on the other side of the card

Thinking very minimalistic and modern.
I don't have a particular font i mind or how to capitalize my name or website. This card will lead people to my new website that is being designed to showcase my photography and music.

* Initial thought was the front side of the card having a grid-like pattern built out of dashes or periods, with my website sitting within the pattern and on the back side my email on a stark white background. But that might look completely lame - haha.

I'm looking forward to seeing what you come up with.

thank you,
- ted marlow

Reason: Want to spend some more time with the designs and add a little $. thanks for all the designs - ted

Wanted to add a little $ and spend some more time with the designs.

big thanks to all who have submitted work 

- ted

www.tedmarlow.com
ted@tedmarlow.com

000000
ffffff

• tedmarlow.com
ted@tedmarlow.com
• phone number
any description of what i do, photography or music

```html
<!DOCTYPE html>
<html lang="en">
<head>
<meta charset="utf-8">
<title>Ted Marlow — Business Card</title>
<link rel="stylesheet" href="https://fonts.googleapis.com/css2?family=Open+Sans:wght@400;700&display=swap">
<style>
  :root {
    --backdrop: #e4e4e4;
    --card: #ffffff;
    --ink: #000000;
    --edge: #d2d2d2;
  }
  html, body {
    margin: 0;
    padding: 0;
    width: 1200px;
    height: 1200px;
    overflow: hidden;
    background: var(--backdrop);
    font-family: "Open Sans", Arial, sans-serif;
  }
  .canvas {
    position: relative;
    width: 1200px;
    height: 1200px;
    display: flex;
    flex-direction: column;
    align-items: center;
    justify-content: center;
    gap: 60px;
  }
  .card {
    position: relative;
    width: 700px;
    height: 400px;
    background: var(--card);
    color: var(--ink);
    box-shadow: 0 0 0 1px var(--edge), 0 12px 30px rgba(0,0,0,0.12);
    box-sizing: border-box;
  }
  .card__name {
    position: absolute;
    left: 62px;
    top: 36px;
    margin: 0;
    font-weight: 700;
    font-size: 56px;
    line-height: 1.08;
    letter-spacing: 0.5px;
  }
  .card__contact {
    position: absolute;
    left: 64px;
    bottom: 52px;
    margin: 0;
    font-weight: 400;
    font-size: 28px;
    letter-spacing: 7px;
  }
</style>
</head>
<body>
  <main class="canvas">
    <section class="card card--front" aria-label="Card front">
      <h1 class="card__name">Ted<br>Marlow</h1>
      <p class="card__contact">www.TedMarlow.com</p>
    </section>
    <section class="card card--back" aria-label="Card back">
      <p class="card__contact">Ted@TedMarlow.com</p>
    </section>
  </main>
</body>
</html>
```